Little Grins Dental Business Card

I need a business card designed for a dentist who works exclusively with children.
We prefer designs that are out of ordiary that is fun and interesting to kids.

there is no logo since this is a dentists office. The name of the doctor is "Tavor Kesh" if you want to get creative with that.

Target Market(s)

Kids

Industry/Entity Type

Business

Contact Information for Business Card

Anythings that is creative

Colors

Designer to choose colors to be used in the design.

```html
<!DOCTYPE html>
<html lang="en">
<head>
<meta charset="utf-8">
<title>Little Grins Dental – Business Card</title>
<link rel="stylesheet" href="https://fonts.googleapis.com/css2?family=Questrial&family=Open+Sans:wght@400;600;700&display=swap">
<style>
  :root {
    --bg: #eceae6;
    --card: #ffffff;
    --ink: #222222;
    --grey: #8a8a8a;
    --rule: #9a9a9a;
    --green: #a5cd39;
    --blue: #1ba8e0;
  }
  * { margin: 0; padding: 0; box-sizing: border-box; }
  html, body { width: 1200px; height: 900px; overflow: hidden; }
  body {
    background: var(--bg);
    font-family: "Open Sans", sans-serif;
    color: var(--ink);
    position: relative;
  }
  .card {
    position: absolute;
    left: 250px;
    width: 700px;
    height: 400px;
    background: var(--card);
    box-shadow: 0 6px 18px rgba(0,0,0,0.18);
    overflow: hidden;
  }
  .card--back { top: 30px; }
  .card--front { top: 470px; }

  /* back side */
  .back-wordmark {
    position: absolute;
    top: 62px;
    left: 0; right: 0;
    text-align: center;
    font-family: "Questrial", sans-serif;
    font-size: 62px;
    color: var(--grey);
    letter-spacing: 1px;
  }
  .appointment-label {
    position: absolute;
    top: 185px;
    left: 0; right: 0;
    text-align: center;
    font-weight: 700;
    font-size: 20px;
    color: var(--grey);
  }
  .appointment-line {
    position: absolute;
    left: 150px;
    width: 400px;
    height: 1px;
    background: var(--rule);
  }
  .appointment-line--one { top: 262px; }
  .appointment-line--two { top: 322px; }

  /* front side */
  .front-shapes { position: absolute; inset: 0; }
  .holder {
    position: absolute;
    top: 34px;
    left: 62px;
  }
  .holder-name {
    font-weight: 700;
    font-size: 22px;
    line-height: 1.1;
  }
  .holder-name .first { color: var(--green); }
  .holder-name .last { color: var(--blue); }
  .holder-title { font-size: 15px; }
  .contact {
    position: absolute;
    top: 140px;
    left: 34px;
    font-size: 16px;
    line-height: 1.35;
    list-style: none;
  }
  .contact li { display: flex; align-items: center; gap: 8px; }
  .contact .address { padding-left: 0; }
  .contact svg { width: 12px; height: 12px; flex: none; }
  .contact .gap { margin-top: 6px; }
  .front-wordmark {
    position: absolute;
    top: 150px;
    left: 380px;
    display: flex;
    align-items: center;
    gap: 14px;
    font-family: "Questrial", sans-serif;
    font-size: 40px;
    line-height: 1.1;
    color: var(--grey);
  }
  .front-wordmark .dot {
    width: 34px; height: 34px;
    border-radius: 50%;
    background: var(--green);
    flex: none;
  }
</style>
</head>
<body>

<section class="card card--back" aria-label="Card back, appointment reminder">
  <p class="back-wordmark">Little Grins Dental</p>
  <p class="appointment-label">Next Appointment</p>
  <div class="appointment-line appointment-line--one"></div>
  <div class="appointment-line appointment-line--two"></div>
</section>

<section class="card card--front" aria-label="Card front">
  <svg class="front-shapes" viewBox="0 0 700 400" width="700" height="400" aria-hidden="true">
    <polygon points="0,20 42,20 0,50" fill="var(--blue)"/>
    <polygon points="48,20 58,20 40,60 18,60" fill="var(--green)"/>
    <polygon points="0,290 330,330 322,346 0,346" fill="var(--blue)"/>
    <polygon points="332,332 700,378 700,400 322,400 322,350" fill="var(--green)"/>
  </svg>

  <div class="holder">
    <p class="holder-name"><span class="first">Tavor</span> <span class="last">Kesh</span></p>
    <p class="holder-title">Managing Director</p>
  </div>

  <ul class="contact">
    <li class="address">48 Maple Lane, Suite 2</li>
    <li class="address">Brookfield, 40217.</li>
    <li class="gap">
      <svg viewBox="0 0 12 12"><path d="M2 1h3l1 3-1.5 1a6 6 0 0 0 2.5 2.5L8 6l3 1v3c-5 1-10-4-9-9z" fill="var(--green)"/></svg>
      044-555 210 384
    </li>
    <li>
      <svg viewBox="0 0 12 12"><rect x="1" y="2.5" width="10" height="7" fill="var(--green)"/><path d="M1 2.5l5 4 5-4" stroke="#fff" fill="none"/></svg>
      hello@littlegrins.com
    </li>
    <li>
      <svg viewBox="0 0 12 12"><path d="M5 7l2-2M4 6l-1.5 1.5a2 2 0 0 0 2 2L6 8M8 6l1.5-1.5a2 2 0 0 0-2-2L6 4" stroke="var(--green)" stroke-width="1.4" fill="none"/></svg>
      www.littlegrins.com
    </li>
  </ul>

  <div class="front-wordmark">
    <span class="dot"></span>
    <span>Little Grins<br>Dental</span>
  </div>
</section>

</body>
</html>
```